Home page for Quill Helper

Develop the home page for QuillHelper.co, which is an AI-powered chatbot platform that allows users to add an educated chatbot to their websites to assist customers with questions and other inquiries.

The hero banner should contain the text:

"Instantly create a FREE AI Chatbot for your website! Just enter the URL of your website below and the chatbot will educate itself about your business"

Below this text should be an text box to enter the URL of the visitor's website.

The platform is a subsidiary of PageLoomX.com, so the theme should be very similar to the website pageloomx.com.

I have attached the content for the page, a mockup of the hero banner section, and videos for the hero banner.

```html
<!DOCTYPE html>
<html lang="en">
<head>
<meta charset="UTF-8">
<title>Quill Helper – Intelligent Support For Your Business</title>
<link href="https://fonts.googleapis.com/css2?family=Barlow:wght@300;400;500;600;700;800&family=Poppins:wght@400;500;600&display=swap" rel="stylesheet">
<style>
:root{
  --navy:#062443;
  --navy-deep:#041a33;
  --blue:#1f6fe5;
  --blue-light:#3b8cf5;
  --red:#f0453d;
  --ink:#0d1f33;
  --muted:#56657a;
  --pale:#f2f5f9;
  --line:#e2e8f0;
  --white:#ffffff;
}
*{margin:0;padding:0;box-sizing:border-box}
html,body{width:1200px;height:5240px;overflow:hidden}
body{font-family:"Poppins",sans-serif;color:var(--ink);background:var(--white);position:relative}
.abs{position:absolute}
h1,h2,h3{font-family:"Barlow",sans-serif;text-transform:uppercase;line-height:1.05}
.light{font-weight:300}
.eyebrow{font-family:"Barlow",sans-serif;font-weight:700;font-size:10px;letter-spacing:1.5px;color:var(--blue);text-transform:uppercase}
.btn-red{display:inline-block;background:var(--red);color:#fff;font-family:"Barlow",sans-serif;font-weight:600;font-size:11px;padding:10px 18px;border-radius:2px;white-space:nowrap}
.btn-blue{display:inline-block;background:var(--blue);color:#fff;font-family:"Barlow",sans-serif;font-weight:600;font-size:11px;padding:9px 14px;border-radius:2px;white-space:nowrap}
p{font-size:11px;line-height:1.75;color:var(--muted)}
.art{border-radius:8px}

/* hero */
.hero{left:0;top:0;width:1200px;height:680px;background:linear-gradient(160deg,var(--navy) 40%,#0a3a66 100%)}
.nav{left:122px;top:32px;width:956px;height:30px;display:flex;align-items:center}
.brand{font-family:"Barlow",sans-serif;font-weight:700;font-size:16px;color:#fff;letter-spacing:.5px}
.nav ul{list-style:none;display:flex;gap:22px;position:absolute;left:296px;top:8px}
.nav li{font-family:"Barlow",sans-serif;font-weight:500;font-size:11px;color:#fff;white-space:nowrap}
.nav .actions{position:absolute;right:0;display:flex;gap:10px}
.hero-art{left:620px;top:60px;width:500px;height:540px;background:radial-gradient(ellipse at 45% 45%,#3ad2ff 0%,#1380c8 35%,rgba(6,36,67,0) 72%);border-radius:50%}
.hero h1{left:120px;top:232px;font-size:52px;color:#fff;font-weight:700}
.hero .lead{left:120px;top:352px;width:500px;color:#dbe7f5;font-size:10.5px}
.url-box{left:120px;top:408px;width:492px;height:40px;background:#fff;border-radius:3px;display:flex;align-items:center;padding:0 4px 0 12px}
.url-box span{font-size:10px;color:#7b8794;flex:1;display:flex;gap:6px;align-items:center}
.checks{left:120px;top:462px;display:flex;gap:26px}
.checks div{font-size:9px;color:#dbe7f5;display:flex;gap:6px;align-items:center}

/* benefits */
.benefit{top:625px;width:305px;height:150px;background:#fff;border-radius:4px;box-shadow:0 8px 24px rgba(6,36,67,.12);text-align:center;padding-top:32px}
.benefit h3{font-size:15px;font-weight:600;margin-top:16px;padding:0 22px}

/* welcome */
.welcome-art{left:205px;top:820px;width:410px;height:380px;background:linear-gradient(135deg,#e9f0fb,#c9dcf5 60%,#f8d6d2)}
.welcome-text{left:651px;top:862px;width:440px}
.welcome-text h2{font-size:40px;font-weight:700;margin:8px 0 20px;white-space:nowrap}
.welcome-text p{margin-bottom:16px}

/* features */
.features{left:0;top:1250px;width:1200px;height:515px;background:var(--pale)}
.section-title{width:1200px;text-align:center}
.section-title h2{font-size:40px;font-weight:700;margin-top:8px}
.feature{top:1425px;width:305px;height:275px;background:#fff;border:1px solid var(--line);padding:26px 22px}
.feature h3{font-size:15px;font-weight:600;margin:14px 0 12px}
.feature p{font-size:9.5px;line-height:1.75;margin-bottom:10px}
.feature b{color:var(--ink);font-weight:600}

/* steps */
.step{width:370px}
.step h2{font-size:32px;font-weight:700;margin-bottom:22px;white-space:nowrap}
.step ul{list-style:none;margin:14px 0}
.step li{font-size:10px;line-height:1.7;color:var(--muted);padding-left:20px;position:relative;margin-bottom:14px}
.step li::before{content:"";position:absolute;left:2px;top:3px;width:8px;height:4px;border-left:2px solid var(--blue);border-bottom:2px solid var(--blue);transform:rotate(-45deg)}
.step li b{color:var(--ink);font-weight:600}
.step-art{background:linear-gradient(135deg,#eaf1fc,#c3d8f6 55%,#f6d3cf)}

/* testimonials */
.testimonials{left:0;top:3265px;width:1200px;height:365px;background:var(--pale)}
.quote{top:3310px;width:280px;height:280px;background:#fff;border:1px solid var(--line);text-align:center;padding:0 20px}
.avatar{width:100px;height:100px;border-radius:50%;margin:-30px auto 18px;background:linear-gradient(135deg,#c99a7a,#6b4b3a)}
.quote q{display:block;font-family:"Barlow",sans-serif;font-weight:600;font-size:15px;line-height:1.35;quotes:"\201C" "\201D"}
.quote .who{margin-top:18px;font-family:"Barlow",sans-serif;font-size:13px;font-weight:700}
.quote .who span{font-weight:400;font-size:10px;color:var(--muted)}
.dots{left:386px;top:3612px;display:flex;gap:6px}
.dots i{width:6px;height:6px;border-radius:50%;background:#c9d2de}
.dots i.on{background:var(--ink)}

/* try */
.try{left:0;top:3660px;width:1200px;height:410px;background:var(--navy-deep)}
.try-art{left:620px;top:3660px;width:580px;height:410px;background:radial-gradient(ellipse at 55% 50%,#2b9be0 0%,#0f4f8a 40%,rgba(4,26,51,0) 75%)}
.try-text{left:122px;top:3712px;width:430px}
.try-text h2{font-size:40px;color:#fff;font-weight:700;margin:8px 0 20px;white-space:nowrap}
.try-text p{color:#d3dded;font-size:10.5px;margin-bottom:16px}

/* faq */
.faq-list{left:265px;top:4232px;width:670px}
.faq{border:1px solid var(--line);background:#fff;padding:14px 18px;margin-bottom:10px;position:relative}
.faq h4{font-family:"Barlow",sans-serif;font-weight:600;font-size:14px;padding-right:40px;line-height:1.3}
.faq p{font-size:9.5px;margin-top:20px}
.faq .caret{position:absolute;right:18px;top:20px;width:0;height:0;border-left:4px solid transparent;border-right:4px solid transparent;border-top:5px solid var(--ink)}
.faq .caret.up{border-top:none;border-bottom:5px solid var(--ink)}
.faq-note{width:1200px;text-align:center;font-size:8px;color:var(--muted)}
.faq-note u{color:var(--ink)}

/* cta + footer */
.cta-block{left:0;top:4640px;width:1200px;height:600px;background:var(--navy)}
.cta-text{width:1200px;text-align:center}
.cta-text h2{font-size:40px;color:#fff;font-weight:700;margin:8px 0 18px}
.cta-text p{color:#d3dded;font-size:10.5px;width:520px;margin:0 auto 20px}
.footer-rule{left:122px;width:956px;height:1px;background:rgba(255,255,255,.18)}
.foot-col h5{font-family:"Barlow",sans-serif;font-size:13px;font-weight:700;color:#fff;margin-bottom:14px}
.foot-col li{list-style:none;font-size:9px;color:#cdd7e5;margin-bottom:12px}
.foot-col p{color:#cdd7e5;font-size:9px}
.contact-line{display:flex;gap:8px;align-items:flex-start;font-size:9px;color:#cdd7e5;margin-bottom:14px;line-height:1.5}
.legal{font-size:8.5px;color:#cdd7e5}
.social{display:flex;gap:10px}
.social i{width:10px;height:10px;border-radius:50%;background:#fff}
</style>
</head>
<body>

<!-- HERO -->
<section class="abs hero">
  <div class="abs hero-art" role="img" aria-label="Glowing blue circuit-board human head profile"></div>
  <nav class="abs nav">
    <span class="brand">QuillHelper.co</span>
    <ul><li>Home</li><li>About Quill Helper</li><li>Why Choose Us</li><li>FAQs</li><li>Contact Us</li></ul>
    <div class="actions"><span class="btn-red" style="padding:9px 22px">Login</span><span class="btn-blue">Get Started for FREE!</span></div>
  </nav>
  <div class="abs eyebrow" style="left:120px;top:220px">Revolutionize your workflow with AI</div>
  <h1 class="abs">Intelligent <span class="light">Support</span><br>For Your <span class="light">Business.</span></h1>
  <p class="abs lead">Instantly create a FREE AI Chatbot for your website! Just enter the URL of your website below and the chatbot will educate itself about your business.</p>
  <div class="abs url-box">
    <span><svg width="12" height="12" viewBox="0 0 24 24" fill="none" stroke="#7b8794" stroke-width="2"><path d="M10 14a4 4 0 0 0 6 0l3-3a4 4 0 0 0-6-6l-1 1"/><path d="M14 10a4 4 0 0 0-6 0l-3 3a4 4 0 0 0 6 6l1-1"/></svg>Enter you website URL here....</span>
    <span class="btn-blue" style="padding:10px 22px">Try it Today!</span>
  </div>
  <div class="abs checks">
    <div><svg width="10" height="8" viewBox="0 0 10 8"><path d="M1 4l3 3 5-6" stroke="#3b8cf5" stroke-width="1.6" fill="none"/></svg>No credit card needed</div>
    <div><svg width="10" height="8" viewBox="0 0 10 8"><path d="M1 4l3 3 5-6" stroke="#3b8cf5" stroke-width="1.6" fill="none"/></svg>Unlimited time on Free plan</div>
    <div><svg width="10" height="8" viewBox="0 0 10 8"><path d="M1 4l3 3 5-6" stroke="#3b8cf5" stroke-width="1.6" fill="none"/></svg>Cancel anytime</div>
  </div>
  <svg class="abs" style="left:0;bottom:0" width="1200" height="90" viewBox="0 0 1200 90" preserveAspectRatio="none"><path d="M0 90V50C200 10 380 80 620 60S1000 10 1200 30V90Z" fill="#fff"/></svg>
</section>

<div class="abs benefit" style="left:122px">
  <svg width="30" height="30" viewBox="0 0 24 24" fill="none" stroke="#1f6fe5" stroke-width="1.6"><path d="M4 14v-2a8 8 0 0 1 16 0v2"/><rect x="3" y="13" width="4" height="6" rx="1"/><rect x="17" y="13" width="4" height="6" rx="1"/></svg>
  <h3>Enhance your customer support 24/7.</h3>
</div>
<div class="abs benefit" style="left:447px">
  <svg width="30" height="30" viewBox="0 0 24 24" fill="none" stroke="#1f6fe5" stroke-width="1.6"><circle cx="12" cy="12" r="9"/><path d="M12 7v5l3 2"/></svg>
  <h3>Save your time by automating repetitive inquiries.</h3>
</div>
<div class="abs benefit" style="left:773px">
  <svg width="30" height="30" viewBox="0 0 24 24" fill="none" stroke="#1f6fe5" stroke-width="1.6"><circle cx="8" cy="10" r="4"/><circle cx="16" cy="10" r="4"/><path d="M2 20c1-3 4-4 6-4M22 20c-1-3-4-4-6-4"/></svg>
  <h3>Improve your customer satisfaction, engagement.</h3>
</div>

<!-- WELCOME -->
<div class="abs art welcome-art" role="img" aria-label="Isometric illustration of a robot assistant at a laptop with a person and planning notes"></div>
<div class="abs welcome-text">
  <div class="eyebrow">Welcome to Quill Helper</div>
  <h2>Your business’s<br><span class="light">ultimate</span> AI <span class="light">assistant!</span></h2>
  <p>Imagine having a tireless assistant that’s always ready to interact with your customers, answer their questions, and guide them through their journey on your website. Meet Quill Helper – the fastest and easiest way to create an intelligent AI Agent for your business in just a few minutes.</p>
  <p>Whether you’re a small business owner, a growing enterprise, or a digital agency, Quill Helper is here to revolutionize customer support for you.</p>
  <span class="btn-red">Know More About Us</span>
</div>

<!-- FEATURES -->
<section class="abs features"></section>
<div class="abs section-title" style="left:0;top:1302px">
  <div class="eyebrow">The AI advantage</div>
  <h2>Advanced <span class="light">features</span> that<br>set Quill Helper <span class="light">apart</span></h2>
</div>
<div class="abs feature" style="left:122px">
  <svg width="28" height="28" viewBox="0 0 24 24" fill="none" stroke="#1f6fe5" stroke-width="1.6"><path d="M6 16V11a6 6 0 0 1 12 0v5l2 2H4z"/><path d="M10 20a2 2 0 0 0 4 0"/></svg>
  <h3>Real-time notifications</h3>
  <p>Stay on top of customer interactions with text and email alerts for new inquiries. Never miss a chance to connect with your customers, whether you’re in the office or on the go.</p>
</div>
<div class="abs feature" style="left:447px">
  <svg width="28" height="28" viewBox="0 0 24 24" fill="none" stroke="#1f6fe5" stroke-width="1.6"><rect x="3" y="5" width="18" height="16" rx="2"/><path d="M3 10h18M8 3v4M16 3v4"/></svg>
  <h3>Customizable plans</h3>
  <p>Quill Helper is designed for businesses of all sizes</p>
  <p><b>Free Plan:</b> Perfect for smaller or newer businesses.</p>
  <p><b>Business Plans:</b> Scaled for growing enterprises with advanced features.</p>
  <p><b>Agency Plan:</b> Allows unlimited chatbot creation for digital agencies.</p>
</div>
<div class="abs feature" style="left:773px">
  <svg width="28" height="28" viewBox="0 0 24 24" fill="none" stroke="#1f6fe5" stroke-width="1.6"><rect x="7" y="2" width="10" height="20" rx="2"/><path d="M11 18h2"/></svg>
  <h3>Mobile app access</h3>
  <p>Monitor your bot’s activity and interact with customers directly through our mobile app. Whether you’re at a meeting or traveling, you’re always connected.</p>
</div>

<!-- STEPS -->
<div class="abs section-title" style="left:0;top:1812px">
  <div class="eyebrow">How it works</div>
  <h2>The 3 simple steps <span class="light">to launch</span><br>your <span class="light">Quill Helper</span></h2>
</div>

<div class="abs step" style="left:183px;top:1975px">
  <h2>Step 1: <span class="light">Educate</span> your<br>Quill Helper.</h2>
  <p>Enter the URL of your website, and let Quill Helper do the heavy lifting. The bot will crawl your site and educate itself about your business. Choose from flexible crawling options:</p>
  <ul>
    <li><b>Home Page Only:</b> Ideal for a quick setup with basic information.</li>
    <li><b>Specific Sub-Pages:</b> Focus on important sections like FAQs, pricing, or services.</li>
    <li><b>All Pages:</b> For a comprehensive AI assistant that knows your business inside-out.</li>
  </ul>
  <p>The more pages the bot crawls, the smarter it becomes, ensuring it provides accurate and helpful responses to your customers.</p>
</div>
<div class="abs art step-art" style="left:610px;top:1975px;width:410px;height:350px" role="img" aria-label="Isometric robot using a laptop surrounded by books and documents"></div>

<svg class="abs" style="left:590px;top:2330px" width="100" height="120" viewBox="0 0 100 120"><path d="M95 2C40 10 20 50 25 100" stroke="#9fb3cc" stroke-dasharray="3 3" fill="none"/><path d="M14 92l12 20 8-22z" fill="#1f6fe5"/></svg>

<div class="abs art step-art" style="left:183px;top:2375px;width:400px;height:380px" role="img" aria-label="Isometric robot on a ladder building a website with a person holding a wrench"></div>
<div class="abs step" style="left:653px;top:2428px">
  <h2>Step 2: <span class="light">Customize</span> your<br>Quill Helper.</h2>
  <p>Make your bot uniquely yours! Personalize it by:</p>
  <ul>
    <li><b>Giving it a name that represents your brand.</b></li>
    <li><b>Choosing an avatar to align with your website’s design.</b></li>
    <li><b>Uploading additional knowledge such as documents, spreadsheets, and FAQs to enrich its database.</b></li>
  </ul>
  <p>The more information you provide, the smarter and more efficient your bot becomes in handling customer inquiries.</p>
</div>

<svg class="abs" style="left:520px;top:2790px" width="120" height="110" viewBox="0 0 120 110"><path d="M5 2C70 10 95 40 95 90" stroke="#9fb3cc" stroke-dasharray="3 3" fill="none"/><path d="M82 84l20 12-4-24z" fill="#1f6fe5"/></svg>

<div class="abs step" style="left:183px;top:2855px;width:400px">
  <h2>Step 3: Activate and<br><span class="light">deploy your</span> Quill Helper</h2>
  <p>You’re just one step away from transforming your customer support experience! Here’s how you go live:</p>
  <ul>
    <li><b>Enable the optional Human Assistance Mode:</b> allowing you or your team to step in for direct customer interaction. Configure this feature manually or set a schedule, like business hours for personal assistance and after-hours AI responses.</li>
    <li>Copy the unique HTML code generated for your bot.</li>
    <li>Paste the code into your website.</li>
  </ul>
  <p>And just like that, your Quill Helper comes alive on your website, ready to interact with visitors and provide seamless support!</p>
</div>
<div class="abs art step-art" style="left:630px;top:2810px;width:400px;height:390px" role="img" aria-label="Isometric robot on a screen greeting people with a megaphone and chat bubbles"></div>

<!-- TESTIMONIALS -->
<section class="abs testimonials"></section>
<div class="abs quote" style="left:122px;top:3340px;height:260px">
  <div class="avatar" role="img" aria-label="Portrait photo of a smiling small business owner"></div>
  <q>Quill Helper transformed our customer support. It’s like having an extra team member who works 24/7!</q>
  <div class="who">Dana K., <span>Small Business Owner</span></div>
</div>
<div class="abs quote" style="left:415px;top:3340px;height:260px">
  <div class="avatar" role="img" aria-label="Portrait photo of a smiling enterprise manager"></div>
  <q>The human assistance option is a game-changer. Our team loves the flexibility of jumping in when needed.</q>
  <div class="who">Omar L., <span>Enterprise Manager</span></div>
</div>
<div class="abs dots"><i></i><i class="on"></i><i></i><i></i></div>
<div class="abs" style="left:737px;top:3352px;width:360px">
  <div class="eyebrow">Don’t just take our word for it</div>
  <h2 style="font-size:40px;font-weight:700;margin:8px 0 20px">Why businesses<br>love <span class="light">Quill Helper</span></h2>
  <p style="margin-bottom:20px">Artificial Intelligence (AI) has swiftly transitioned from the pages of science fiction to an integral part of our daily lives. We see its effects everywhere. People love us always.</p>
  <span class="btn-red">Know More About Us</span>
</div>

<!-- TRY FREE -->
<section class="abs try"></section>
<div class="abs try-art" role="img" aria-label="Blue digital human head profile made of glowing data points"></div>
<div class="abs try-text">
  <div class="eyebrow" style="color:#3b8cf5">Don’t just take our word for it</div>
  <h2>Try Quill <span class="light">Helper now</span><br>– It’s free!</h2>
  <p>Are you ready to elevate your business with the power of AI? Getting started is as easy as entering your website URL into the box below. Within minutes, your Quill Helper will be ready to take your customer support to the next level.</p>
  <p>Don’t wait to experience the future of customer interaction. Try Quill Helper now for free and watch your business grow effortlessly. Click the button below to start your journey with Quill Helper.</p>
  <span class="btn-red">Get Started for FREE!</span>
</div>

<!-- FAQ -->
<div class="abs section-title" style="left:0;top:4115px">
  <div class="eyebrow">Frequently ask questions</div>
  <h2>Instant answers <span class="light">to your queries</span></h2>
</div>
<div class="abs faq-list">
  <div class="faq" style="padding-bottom:18px"><h4>How long does it take to set up Quill Helper?</h4><i class="caret up"></i><p>You can have your Quill Helper live on your website in just a few minutes. The setup process is quick and user-friendly.</p></div>
  <div class="faq"><h4>Is there a free plan available?</h4><i class="caret"></i></div>
  <div class="faq"><h4>What if I want to interact directly with some customers without the bot’s assistance?</h4><i class="caret"></i></div>
  <div class="faq"><h4>Can I add my own content to the bot’s knowledgebase?</h4><i class="caret"></i></div>
</div>
<div class="abs" style="left:527px;top:4530px"><span class="btn-red" style="padding:11px 30px">View More FAQs</span></div>
<div class="abs faq-note" style="left:0;top:4580px">*If you can’t find the answer for what you are looking for below, please contact one of our <u>support managers</u></div>

<!-- CTA + FOOTER -->
<section class="abs cta-block"></section>
<svg class="abs" style="left:0;top:4620px" width="1200" height="90" viewBox="0 0 1200 90" preserveAspectRatio="none"><path d="M0 0H1200V40C1000 10 820 70 600 50S200 0 0 40Z" fill="#fff"/></svg>
<div class="abs cta-text" style="left:0;top:4740px">
  <div class="eyebrow" style="color:#3b8cf5">Stop waiting. Start building.</div>
  <h2>Start your journey with<br><span class="light">Quill Helper</span> today!</h2>
  <p>See why businesses of all sizes trust us to handle their customer support needs. Your intelligent AI assistant is just a few clicks away – try it now!</p>
  <span class="btn-red" style="padding:11px 24px">Get Started for FREE!</span>
</div>
<div class="abs footer-rule" style="top:4965px"></div>

<div class="abs foot-col" style="left:122px;top:4990px;width:240px">
  <div class="brand" style="margin-bottom:12px">QuillHelper.co</div>
  <p style="line-height:1.7">We understand you want a transformation partner to go the whole distance – to deliver transformation that works from day one and continues to work long after we’ve gone.</p>
</div>
<div class="abs" style="left:415px;top:4990px;width:1px;height:150px;background:rgba(255,255,255,.18)"></div>
<div class="abs foot-col" style="left:484px;top:4990px">
  <h5>Company</h5><ul><li>About Us</li><li>Our team</li><li>Job opportunities</li><li>Contact Us</li><li>Legal</li></ul>
</div>
<div class="abs foot-col" style="left:685px;top:4990px">
  <h5>Resources</h5><ul><li>Our Blog</li><li>Contact Support</li><li>Contact Sales</li><li>Developers</li></ul>
</div>
<div class="abs foot-col" style="left:920px;top:4990px;width:160px">
  <h5>Contact us</h5>
  <div class="contact-line"><svg width="10" height="12" viewBox="0 0 10 12"><path d="M5 0a4 4 0 0 1 4 4c0 3-4 8-4 8S1 7 1 4a4 4 0 0 1 4-4z" fill="#fff"/><circle cx="5" cy="4" r="1.5" fill="#062443"/></svg><span>218 Birch Lane, Fairview<br>Sample street line</span></div>
  <div class="contact-line"><svg width="10" height="10" viewBox="0 0 24 24"><path d="M6 2l4 4-2 3a12 12 0 0 0 7 7l3-2 4 4-3 4C10 22 2 14 2 5z" fill="#fff"/></svg><span>Call Us: +100-5550199</span></div>
  <div class="contact-line"><svg width="11" height="9" viewBox="0 0 22 16"><rect width="22" height="16" rx="2" fill="#fff"/><path d="M1 1l10 8 10-8" stroke="#062443" stroke-width="2" fill="none"/></svg><span>Email: hello@QuillHelper.co</span></div>
</div>
<div class="abs footer-rule" style="top:5175px"></div>
<div class="abs legal" style="left:122px;top:5200px">© 2023 QuillHelper.co &nbsp;|&nbsp; All rights reserved.</div>
<div class="abs social" style="left:576px;top:5200px"><i></i><i></i><i></i></div>
<div class="abs legal" style="left:890px;top:5200px">Terms of Use &nbsp;|&nbsp; Data Privacy &nbsp;|&nbsp; Disclaimer</div>

</body>
</html>
```